Torvale Works- Plumbing Business Card

We need a business card design for a new company that services Canberra and surrounds. We are a professional family-owned plumbing company who has 20+ years' experience. We would like to use our logo as well as the colours black, white, grey and the signature green. The final design needs to communicate professional, high-end, plumbing with reliable service. We provide obligation free quotes and are open 24/7. Services include: Bathroom/kitchen renovations, drainage, stormwater, water leaks, plumbing maintenance, water tanks and septics.

Target Market(s)

Homeowners, real estate agents, builders, small business owners

Industry/Entity Type

Plumbing & Construction

Font styles to use
Serif
Sans Serif

Colors
59FF00
82FF00
B8FF75
E3FFCB
F4FFEA

Requirements
Must have
• Must have logo, example of services and contact details

```html
<!DOCTYPE html>
<html lang="en">
<head>
<meta charset="utf-8">
<title>Torvale Works – Business Card</title>
<link href="https://fonts.googleapis.com/css2?family=Montserrat:wght@400;500;700;800&family=Roboto:wght@400;700&display=swap" rel="stylesheet">
<style>
  :root {
    --bg: #2a2a2a;
    --card: #000000;
    --green: #06a006;
    --band: #02a402;
    --white: #ffffff;
  }
  * { box-sizing: border-box; margin: 0; padding: 0; }
  html, body { width: 1200px; height: 757px; overflow: hidden; background: var(--bg); }
  .canvas { position: relative; width: 1200px; height: 757px; }

  .card {
    position: absolute; top: 233px; width: 486px; height: 291px;
    background: var(--card); overflow: hidden;
    box-shadow: 0 6px 18px rgba(0,0,0,.55);
  }
  .card--front { left: 99px; }
  .card--back { left: 615px; }

  .brand {
    position: absolute; font-family: "Montserrat", sans-serif; font-weight: 800;
    color: var(--green); text-transform: uppercase; line-height: .95; letter-spacing: .5px;
  }
  .card--front .brand { left: 35px; top: 112px; width: 172px; font-size: 34px; text-align: center; }
  .card--back .brand { left: 0; right: 0; top: 58px; font-size: 34px; text-align: center; }

  .person { position: absolute; left: 236px; top: 66px; font-family: "Montserrat", sans-serif; }
  .person__name { color: var(--green); font-weight: 700; font-size: 22.5px; letter-spacing: .3px; line-height: 1; }
  .person__role { color: var(--white); font-size: 12px; margin-top: 3px; letter-spacing: .2px; }

  .contact { position: absolute; left: 236px; font-family: "Montserrat", sans-serif; font-size: 12.2px; color: var(--white); display: flex; align-items: flex-start; gap: 5px; line-height: 14px; letter-spacing: .1px; }
  .contact--address { top: 125px; }
  .contact--phone { top: 171px; }
  .contact--email { top: 192px; }
  .contact--web { top: 213px; }
  .contact__icon { width: 15px; height: 15px; flex: none; }

  .rule { position: absolute; left: 0; right: 0; top: 259px; height: 2px; background: var(--green); }

  .services-band { position: absolute; left: 0; right: 0; top: 195px; bottom: 0; background: var(--band); }
  .services-line { position: absolute; left: 0; right: 0; top: 192px; height: 1.5px; background: var(--band); }
  .services-title {
    position: absolute; left: 152px; top: 183px; width: 182px; height: 24px;
    background: var(--card); border-radius: 0 0 10px 10px;
    font-family: "Roboto", sans-serif; font-weight: 700; font-size: 15.5px; color: var(--white);
    text-align: center; line-height: 24px; letter-spacing: -.2px;
  }
  .services-list { position: absolute; top: 216px; list-style: none; font-family: "Roboto", sans-serif; font-size: 12px; color: var(--white); line-height: 16.5px; }
  .services-list li { position: relative; padding-left: 8px; }
  .services-list li::before { content: ""; position: absolute; left: 0; top: 7px; width: 3px; height: 3px; border-radius: 50%; background: var(--white); }
  .services-list--left { left: 85px; }
  .services-list--right { left: 269px; }
</style>
</head>
<body>
<main class="canvas">

  <section class="card card--front" aria-label="Card front">
    <div class="brand">Torvale<br>Works</div>

    <div class="person">
      <div class="person__name">DANA WHITLOW</div>
      <div class="person__role">CEO/Manger</div>
    </div>

    <div class="contact contact--address">
      <svg class="contact__icon" viewBox="0 0 16 16"><rect width="16" height="16" rx="2" fill="var(--green)"/><path d="M8 2.8a3.6 3.6 0 0 0-3.6 3.6c0 2.7 3.6 6.8 3.6 6.8s3.6-4.1 3.6-6.8A3.6 3.6 0 0 0 8 2.8zm0 5a1.4 1.4 0 1 1 0-2.8 1.4 1.4 0 0 1 0 2.8z" fill="#fff"/></svg>
      <span>48 Ridge View Rd. Suite<br>12 Canberra, ACT 2600</span>
    </div>
    <div class="contact contact--phone">
      <svg class="contact__icon" viewBox="0 0 16 16"><rect width="16" height="16" rx="2" fill="var(--green)"/><path d="M5.2 3.2l1.6 2.2-1 1.1c.7 1.5 1.9 2.7 3.4 3.4l1.1-1 2.2 1.6-.8 1.9C7.4 12.3 3.7 8.6 3.3 4z" fill="#fff"/></svg>
      <span>002-555-0190</span>
    </div>
    <div class="contact contact--email">
      <svg class="contact__icon" viewBox="0 0 16 16"><rect width="16" height="16" rx="2" fill="var(--green)"/><rect x="3" y="4.5" width="10" height="7" fill="#fff"/><path d="M3 4.5l5 4 5-4M3 11.5l3.7-3.2M13 11.5L9.3 8.3" stroke="var(--green)" stroke-width="1" fill="none"/></svg>
      <span>info@torvaleworks.com</span>
    </div>
    <div class="contact contact--web">
      <svg class="contact__icon" viewBox="0 0 16 16"><rect width="16" height="16" rx="2" fill="var(--green)"/><path d="M5 3v9l2.3-2.1 1.5 3.2 1.4-.7-1.5-3.1H12z" fill="#fff"/></svg>
      <span>TorvaleWorks.com</span>
    </div>

    <div class="rule"></div>
  </section>

  <section class="card card--back" aria-label="Card back">
    <div class="brand">Torvale<br>Works</div>

    <div class="services-line"></div>
    <div class="services-band"></div>
    <div class="services-title">24/7. Services include:</div>

    <ul class="services-list services-list--left">
      <li>Bathroom/kitchen renovations</li>
      <li>Drainage</li>
      <li>Stormwater</li>
    </ul>
    <ul class="services-list services-list--right">
      <li>Water leaks</li>
      <li>Plumbing maintenance</li>
      <li>Water tanks and septics</li>
    </ul>
  </section>

</main>
</body>
</html>
```